Marlowe Solutions Business Card

We need a business card design for a software and IT consulting company called marlowe solutions. We would like to feature a kinkajou (it is a small tree-dwelling animal) somewhere in the design. We would like a green color involved somewhere (but not overwhelming). Back of card should be predominately a color, front of the card can be predominately white or predominately a different color than the back.

Information on front of card:

Contact information:
Phone: (555) 214-3907
Email: peter.dunmore@mrlsol.example
Website: www.mrlsol.example

Name: Peter Dunmore
Title: Owner / Developer

Information on back of card:
Marlowe Solutions
Targeted Solutions. Fit to your environment.

Industry/Entity Type

Software

Requirements
Should not have
• Avoid anything that too closely resembles a cartoon or campy feel. This should be professional and modern looking.

```html
<!DOCTYPE html>
<html lang="en">
<head>
<meta charset="utf-8">
<title>Marlowe Solutions Business Card</title>
<link rel="stylesheet" href="https://fonts.googleapis.com/css2?family=Caladea&family=Michroma&family=Roboto+Condensed:ital,wght@1,800;1,900&display=swap">
<style>
  :root {
    --paper: #ffffff;
    --ink: #444444;
    --brand: #16a07d;
    --mint: #55ecc5;
    --forest: #0f6e58;
    --deep: #137a66;
    --bright: #2db08b;
    --card-edge: #b9b9b9;
    --frame: #dcdcdc;
  }
  * { box-sizing: border-box; margin: 0; padding: 0; }
  html, body { width: 1200px; height: 1000px; overflow: hidden; background: var(--paper); }
  .canvas {
    position: relative; width: 1200px; height: 1000px;
    border: 1px solid var(--frame); background: var(--paper);
  }
  .card { position: absolute; width: 620px; height: 391px; }
  .card-front { left: 166px; top: 43px; border: 1px solid var(--card-edge); background: var(--paper); }
  .card-back { left: 343px; top: 454px; height: 390px; }
  .card svg.shapes { position: absolute; left: 0; top: 0; }

  .brand-mark { position: absolute; left: 14px; top: 14px; display: flex; align-items: center; gap: 12px; }
  .brand-mark .mark-square { width: 40px; height: 40px; background: var(--mint); }
  .brand-mark .mark-name {
    font-family: "Caladea", "Cambria", serif; font-size: 26px; line-height: 40px; color: var(--brand);
  }

  .contact {
    position: absolute; right: 28px; top: 186px; text-align: right;
    font-family: "Caladea", "Cambria", serif; color: var(--ink);
  }
  .contact .person { font-size: 40px; line-height: 48px; }
  .contact .role { font-size: 27px; line-height: 34px; color: var(--brand); margin-bottom: 10px; }
  .contact .line { font-size: 24px; line-height: 28px; }
  .contact .phone { font-size: 25px; line-height: 30px; }

  .back-text { position: absolute; font-family: "Michroma", "Arial", sans-serif; color: var(--brand); white-space: nowrap; }
  .company-name { right: 22px; top: 48px; font-size: 32px; letter-spacing: 1px; text-transform: uppercase; line-height: 44px; }
  .tagline { right: 22px; font-size: 13px; letter-spacing: 3px; text-transform: uppercase; }
  .tagline-one { top: 112px; }
  .tagline-two { top: 152px; }

  .illustration-slot {
    position: absolute; left: 455px; top: 184px; width: 128px; height: 198px;
    background: linear-gradient(160deg, rgba(255,255,255,0.5), rgba(255,255,255,0.2));
    border-radius: 6px;
  }

  .title-band { position: absolute; left: 0; top: 900px; width: 1200px; height: 90px; }
  .title-band svg { position: absolute; left: 0; top: 0; }
  .title-band .heading {
    position: absolute; left: 28px; top: 4px; white-space: nowrap;
    font-family: "Roboto Condensed", "Arial Narrow", sans-serif; font-style: italic; font-weight: 900;
    font-size: 72px; line-height: 84px; color: var(--paper); letter-spacing: 2px;
  }
</style>
</head>
<body>
<main class="canvas">

  <section class="card card-front" aria-label="Card front">
    <div class="brand-mark">
      <span class="mark-square"></span>
      <span class="mark-name">Marlowe Solutions</span>
    </div>
    <div class="contact">
      <p class="person">Peter Dunmore</p>
      <p class="role">Owner / Developer</p>
      <p class="line">peter.dunmore@mrlsol.example</p>
      <p class="line">www.mrlsol.example</p>
      <p class="phone">(555) 214-3907</p>
    </div>
  </section>

  <section class="card card-back" aria-label="Card back">
    <svg class="shapes" width="620" height="390" viewBox="0 0 620 390">
      <defs>
        <linearGradient id="backFill" x1="0" y1="1" x2="1" y2="0">
          <stop offset="0" stop-color="var(--deep)"/>
          <stop offset="1" stop-color="var(--bright)"/>
        </linearGradient>
      </defs>
      <rect x="2" y="2" width="616" height="386" fill="url(#backFill)" stroke="var(--forest)" stroke-width="4"/>
      <path d="M12 11 H604 V94 H80 C45 94 12 70 12 38 Z" fill="var(--paper)"/>
      <path d="M237 103 H605 V138 H252 A15 15 0 0 1 237 123 Z" fill="var(--paper)"/>
      <path d="M189 143 H605 V178 H204 A15 15 0 0 1 189 163 Z" fill="var(--paper)"/>
    </svg>
    <p class="back-text company-name">Marlowe Solutions</p>
    <p class="back-text tagline tagline-one">Targeted Solutions</p>
    <p class="back-text tagline tagline-two">Fit to your environment</p>
    <div class="illustration-slot" role="img" aria-label="Illustration of a kinkajou climbing a branch, in white"></div>
  </section>

  <header class="title-band">
    <svg width="1200" height="90" viewBox="0 0 1200 90">
      <defs>
        <linearGradient id="bandFill" x1="0" y1="0" x2="1" y2="0">
          <stop offset="0" stop-color="var(--deep)"/>
          <stop offset="0.75" stop-color="#35d09a"/>
          <stop offset="1" stop-color="var(--deep)"/>
        </linearGradient>
      </defs>
      <path d="M15 5 H890 L925 40 V85 H15 Z" fill="url(#bandFill)"/>
      <path d="M925 32 H1186 V85 H975 Z" fill="url(#bandFill)"/>
    </svg>
    <h1 class="heading">Marlowe Solutions</h1>
  </header>

</main>
</body>
</html>
```